Bref créative
VMB Associates, LLC.Business Card, Stationery,
Envelops,letterhead and fax cover
Professional
Dorian Walsby
President
4720 Hollowmere Parkway
Suite 382
Duluth, Ga. 30418
dwalsby@vmbgroupmail.net
www.vmb-partners-example.com
Please no dark background color. Light gray is acceptable.
This will include the services we offer. Telecom Regulatory, Tax Compliance, Corporate Services, Property Tax and Registered Agent Service
We would like the tag line: Accurate, Efficient On Time some where on the card front or back.
we want to get new business and need a card that will make clients want to contact us. Thank you in advance.

```html
<!DOCTYPE html>
<html lang="en">
<head>
<meta charset="utf-8">
<title>VMB Partners, LLC. — Stationery</title>
<link href="https://fonts.googleapis.com/css2?family=Open+Sans:wght@400;600&display=swap" rel="stylesheet">
<style>
:root{
  --bg:#e9eaec;
  --paper:#ffffff;
  --ink:#2b2b2b;
  --muted:#6b6f75;
  --blue:#1a78c2;
  --blue-dark:#0f4f8a;
  --red:#c8202f;
}
*{margin:0;padding:0;box-sizing:border-box}
html,body{width:1200px;height:720px;overflow:hidden}
body{background:var(--bg);font-family:"Open Sans",Arial,sans-serif;color:var(--ink);position:relative}
.sheet{position:absolute;background:var(--paper);box-shadow:0 2px 8px rgba(0,0,0,.18)}
.company-name{font-weight:600;color:var(--ink);line-height:1.2;letter-spacing:0}

/* business card front */
.card-front{left:40px;top:30px;width:270px;height:155px;border-radius:6px;padding:18px 20px}
.card-front .company-name{font-size:12px;width:100px}
.card-front .person{position:absolute;left:140px;top:18px}
.person-name{font-size:9px;font-weight:600;color:var(--blue-dark)}
.person-title{font-size:7px;color:var(--muted)}
.card-front .address{position:absolute;left:140px;top:52px;font-size:6.5px;line-height:1.45;color:var(--muted)}
.card-front .contacts{position:absolute;left:140px;top:90px;font-size:6.5px;line-height:1.55;color:var(--muted)}
.contacts li{list-style:none;display:flex;align-items:center;gap:4px}
.contacts li::before{content:"";width:5px;height:5px;background:var(--blue);border-radius:1px}

/* business card back */
.card-back{left:330px;top:30px;width:270px;height:155px;border-radius:6px}
.services{position:absolute;left:150px;top:20px;font-size:7.5px;line-height:1.75;color:var(--muted)}
.services li{list-style:none;display:flex;align-items:center;gap:5px}
.services li::before{content:"";width:6px;height:6px;background:var(--blue);border-radius:1px}
.tagline{position:absolute;left:0;right:0;bottom:22px;text-align:center;font-size:10px;font-weight:600;color:var(--ink)}

/* envelope back */
.envelope-back{left:40px;top:222px;width:440px;height:200px}
.envelope-back svg{position:absolute;left:0;top:0}
.envelope-back .company-name{position:absolute;left:0;right:0;top:90px;text-align:center;font-size:12px}

/* envelope front */
.envelope-front{left:110px;top:452px;width:480px;height:230px;padding:30px 28px}
.envelope-front .company-name{font-size:18px}
.envelope-front .address{margin-top:12px;font-size:7px;line-height:1.5;color:var(--muted)}
.envelope-front .corner-art{position:absolute;right:0;bottom:0;width:200px;height:110px;background:linear-gradient(135deg,rgba(255,255,255,0) 30%,rgba(200,32,47,.08) 55%,rgba(26,120,194,.12) 100%)}

/* letterhead */
.letterhead{left:670px;top:22px;width:500px;height:676px;padding:38px 40px}
.letterhead .company-name{font-size:24px}
.letterhead .corner-art{position:absolute;right:0;bottom:0;width:300px;height:300px;background:radial-gradient(circle at 100% 100%,rgba(26,120,194,.14) 0%,rgba(111,182,234,.08) 45%,rgba(200,32,47,.05) 60%,rgba(255,255,255,0) 75%)}
.letterhead .footer{position:absolute;left:40px;right:40px;bottom:30px;display:flex;gap:30px;font-size:7px;line-height:1.5;color:var(--muted)}
</style>
</head>
<body>

<section class="sheet card-front">
  <div class="company-name">VMB Partners, LLC.</div>
  <div class="person">
    <div class="person-name">Dorian Walsby</div>
    <div class="person-title">President</div>
  </div>
  <div class="address">4720 Hollowmere Parkway<br>Suite 382<br>Duluth, Ga. 30418</div>
  <ul class="contacts">
    <li>770.555.0142</li>
    <li>770.555.0187</li>
    <li>404.555.0163</li>
    <li>dwalsby@vmbgroupmail.net</li>
    <li>www.vmb-partners-example.com</li>
  </ul>
</section>

<section class="sheet card-back">
  <ul class="services">
    <li>Telecom Regulatory</li>
    <li>Tax Compliance</li>
    <li>Corporate Services</li>
    <li>Property Tax</li>
    <li>Registered Agent Service</li>
  </ul>
  <p class="tagline">Accurate, Efficient On Time</p>
</section>

<section class="sheet envelope-back">
  <svg width="440" height="200" viewBox="0 0 440 200" aria-hidden="true">
    <defs>
      <linearGradient id="flapBlue" x1="0" y1="0" x2="0" y2="1">
        <stop offset="0" stop-color="#0f4f8a"/>
        <stop offset="1" stop-color="#3a9ae0"/>
      </linearGradient>
    </defs>
    <polygon points="0,0 440,0 220,80" fill="url(#flapBlue)"/>
    <polyline points="0,200 220,110 440,200" fill="none" stroke="#e3e5e8" stroke-width="1"/>
  </svg>
  <div class="company-name">VMB Partners, LLC.</div>
</section>

<section class="sheet envelope-front">
  <div class="company-name">VMB Partners, LLC.</div>
  <div class="address">4720 Hollowmere Parkway<br>Suite 382<br>Duluth, Ga. 30418</div>
  <div class="corner-art" role="img" aria-label="Soft corner decoration of faint red and blue squares"></div>
</section>

<section class="sheet letterhead">
  <div class="company-name">VMB Partners, LLC.</div>
  <div class="corner-art" role="img" aria-label="Soft corner decoration of faint red squares and blue sweeping curves"></div>
  <div class="footer">
    <div>4720 Hollowmere Parkway<br>Suite 382<br>Duluth, Ga. 30418</div>
    <div>770.555.0142<br>770.555.0187<br>404.555.0163<br>dwalsby@vmbgroupmail.net</div>
  </div>
</section>

</body>
</html>
```